Start a weight loss Clinic

build a landing page website using the content from this websites. we want to copy all the content from slimpathcoaching.net but make page look more professional. we dont have a logo yet but url is www.brightvitalitycentre.com
https://clinicwellnessalliancegroup.net/home-page
https://www.slimpathcoaching.net/

Target Market(s)

people looking to open a weightloss clinic or a franchise opportunity

Coding

Number of Pages Required

3 page

Requirements
Must have
• copy all content from other site https://www.slimpathcoaching.net/

```html
<!DOCTYPE html>
<html lang="en">
<head>
<meta charset="utf-8">
<title>Bright Vitality Centre – Start Your Own Weight Loss Clinic</title>
<link href="https://fonts.googleapis.com/css2?family=Titillium+Web:wght@400;600;700&family=Lora:wght@400;500&display=swap" rel="stylesheet">
<style>
:root{
  --navy:#134a8e;
  --red:#c8202f;
  --ink:#1c1c1c;
  --grey-bg:#f4f4f4;
  --footer:#262626;
  --footer-bar:#161616;
  --white:#ffffff;
}
*{margin:0;padding:0;box-sizing:border-box}
html,body{width:1200px;height:4011px;overflow:hidden}
body{font-family:"Titillium Web",sans-serif;color:var(--ink);background:var(--white);position:relative}
.abs{position:absolute}
svg{display:block}
.btn{position:absolute;background:var(--red);color:#fff;font-size:12px;font-weight:600;text-transform:uppercase;display:flex;align-items:center;justify-content:center;border-radius:3px;letter-spacing:.2px}

/* header */
.topbar{left:319px;top:0;width:881px;height:44px;background:var(--navy);color:#fff;font-size:13px;display:flex;align-items:center;padding-left:30px;gap:14px}
.topbar .item{display:flex;align-items:center;gap:8px}
.topbar .sep{width:1px;height:24px;background:rgba(255,255,255,.6)}
.brand{left:64px;top:34px;display:flex;align-items:center;gap:12px}
.brand .name{font-size:24px;line-height:25px;font-weight:700;color:var(--navy)}
.brand .mark{width:40px;height:40px;border-radius:50%;border:3px solid var(--red)}
.nav{left:356px;top:72px;display:flex;gap:25px;font-size:12.5px;font-weight:600;text-transform:uppercase}
.nav-cta{left:866px;top:61px;width:255px;height:39px;font-size:12.5px;gap:10px}

/* hero */
.hero-photo{left:0;top:118px;width:962px;height:567px;
  background:linear-gradient(90deg,#b5654c 0%,#c98a70 5%,#3f4a55 11%,#59636d 16%,#d8dbe0 24%,#f0eeed 42%,#f3f2f2 62%,rgba(255,255,255,0) 100%)}
.hero-copy{left:598px;top:188px;width:470px}
.hero-copy h1{font-size:41px;font-weight:600;line-height:50px;color:var(--ink)}
.hero-copy h1 span{color:var(--navy)}
.hero-copy p{font-size:15px;line-height:23.5px;margin-top:16px}
.hero-copy p.first{margin-top:12px}
.hero-copy strong{font-weight:600}
.hero-btn{left:600px;top:534px;width:137px;height:42px}

/* offer */
.offer-title{left:0;width:1200px;top:775px;text-align:center;font-size:33px;font-weight:600}
.card{top:854px;width:232px;height:260px}
.card p{position:absolute;left:24px;bottom:38px;right:14px;color:#fff;font-size:15px;line-height:21px}
.card-1{background:linear-gradient(180deg,rgba(0,0,0,0) 55%,rgba(0,0,0,.55) 100%),linear-gradient(120deg,#5a5e63 0%,#d9dcdf 40%,#8d8a86 70%,#2e2f33 100%)}
.card-2{background:linear-gradient(180deg,rgba(0,0,0,0) 55%,rgba(0,0,0,.5) 100%),linear-gradient(110deg,#c9c6c1 0%,#eef0f1 35%,#8b929a 65%,#3f454c 100%)}
.card-3{background:linear-gradient(180deg,rgba(0,0,0,0) 55%,rgba(0,0,0,.4) 100%),linear-gradient(180deg,#c9a08a 0%,#d8b29b 45%,#7c9ab7 70%,#4d7198 100%)}
.card-4{background:linear-gradient(180deg,rgba(0,0,0,0) 55%,rgba(0,0,0,.5) 100%),linear-gradient(120deg,#3f5670 0%,#6c85a1 35%,#c9d2db 65%,#8f9aa6 100%)}

/* welcome band */
.welcome{left:0;top:1212px;width:1200px;height:508px;background:var(--navy)}
.welcome-photo{left:131px;top:1270px;width:373px;height:367px;background:linear-gradient(115deg,#c79a80 0%,#e9dccf 30%,#f2f0ee 50%,#3a3d42 72%,#dcdcdc 100%)}
.welcome-frame{left:161px;top:1299px;width:313px;height:308px;border:2px solid #fff}
.welcome-copy{left:600px;top:1280px;width:460px;color:#fff}
.welcome-copy .hi{font-size:19px;font-weight:600;padding-left:10px}
.welcome-copy h2{font-size:33px;font-weight:600;line-height:40px;padding-left:7px}
.welcome-copy .sub{font-size:19px;padding-left:14px;margin-top:4px}
.welcome-copy p{font-size:12px;line-height:17.5px;margin-top:17px}
.welcome-copy p strong{font-weight:600}

/* compare */
.compare-photo{left:599px;top:1720px;width:601px;height:480px;background:linear-gradient(180deg,#ebe9e8 0%,#f4f3f3 25%,#d9ab8c 42%,#cf9c7d 68%,#2aa7df 82%,#1f95cf 100%)}
.compare-title{left:96px;top:1810px;font-size:40px;font-weight:600}
.checks{left:102px;top:1895px;display:grid;grid-template-columns:230px 230px;row-gap:20px;font-size:15px}
.checks li{list-style:none;display:flex;align-items:center;gap:9px;height:19px}
.compare-btn{left:218px;top:2090px;width:138px;height:42px}

/* steps */
.steps{left:0;top:2200px;width:1200px;height:610px;background:var(--grey-bg)}
.easy{left:0;width:1200px;top:2302px;text-align:center;font-family:"Lora",serif;font-size:20px;color:var(--navy)}
.steps-title{left:0;width:1200px;top:2336px;text-align:center;font-size:33px;font-weight:600}
.step{width:300px;text-align:center}
.step .disc{width:92px;height:92px;border-radius:50%;background:#fff;margin:0 auto;position:relative;box-shadow:0 3px 10px rgba(0,0,0,.12);display:flex;align-items:center;justify-content:center}
.step .num{position:absolute;left:-10px;top:6px;width:26px;height:26px;border-radius:50%;background:var(--red);color:#fff;font-size:11px;display:flex;align-items:center;justify-content:center;font-weight:600}
.step h3{font-size:27px;font-weight:600;margin-top:6px;line-height:34px}
.step p{font-size:15.5px;line-height:21px;margin-top:4px}
.steps-btn{left:537px;top:2700px;width:137px;height:42px}

/* contact */
.contact-photo{left:0;top:3119px;width:579px;height:549px;background:linear-gradient(180deg,#e4e6ea 0%,#eef0f3 25%,#f5f5f5 45%,#3a3c42 72%,#2a2c31 88%,#e3e5e8 100%)}
.contact-panel{left:579px;top:3119px;width:621px;height:549px;background:var(--red)}
.contact-kicker{left:646px;top:3196px;font-family:"Lora",serif;font-size:20px;color:#fff}
.contact-title{left:646px;top:3222px;font-size:33px;font-weight:600;color:#fff}
.field{position:absolute;background:#fff;color:#555;font-size:15px;padding:9px 11px;height:43px}
.submit{position:absolute;left:645px;top:3582px;width:138px;height:40px;background:var(--navy);color:#fff;font-size:12px;font-weight:600;display:flex;align-items:center;justify-content:center;border-radius:3px}

/* footer */
.footer{left:0;top:3668px;width:1200px;height:284px;background:var(--footer)}
.foot-brand{left:113px;top:3724px;display:flex;align-items:center;gap:12px}
.foot-brand .name{font-size:24px;line-height:25px;font-weight:700;color:#fff}
.foot-brand .mark{width:40px;height:40px;border-radius:50%;border:3px solid #fff}
.foot-h{font-size:15.5px;font-weight:600;color:#fff}
.foot-row{display:flex;gap:12px;font-size:12.5px;line-height:20px;color:#fff}
.quick{font-size:12.5px;line-height:25px;text-transform:uppercase;color:#fff}
.social{display:flex;gap:22px}
.social span{width:23px;height:23px;border-radius:50%;background:#fff;display:block}
.copyright{left:0;top:3952px;width:1200px;height:59px;background:var(--footer-bar);color:#ddd;font-size:12px;display:flex;align-items:center;justify-content:center}
</style>
</head>
<body>

<!-- Header -->
<div class="abs topbar">
  <div class="item">
    <svg width="15" height="15" viewBox="0 0 24 24" fill="none" stroke="#fff" stroke-width="2"><path d="M12 22s7-7 7-12a7 7 0 0 0-14 0c0 5 7 12 7 12z"/><circle cx="12" cy="10" r="2.5"/></svg>
    4410 Meadow Crest Road Suite 210, Lakeview, GA 30190
  </div>
  <div class="sep"></div>
  <div class="item">
    <svg width="15" height="15" viewBox="0 0 24 24" fill="none" stroke="#fff" stroke-width="2"><path d="M22 17v4a1 1 0 0 1-1 1A19 19 0 0 1 2 3a1 1 0 0 1 1-1h4l2 5-2.5 1.5a11 11 0 0 0 6 6L15 12l5 2z"/></svg>
    877-555-0148
  </div>
  <div class="sep"></div>
  <div class="item">
    <svg width="17" height="14" viewBox="0 0 24 18" fill="none" stroke="#fff" stroke-width="2"><rect x="1" y="1" width="22" height="16" rx="2"/><path d="M1 2l11 8 11-8"/></svg>
    hello@slimpathcoaching.net
  </div>
</div>
<div class="abs brand"><span class="name">Bright Vitality<br>Centre</span><span class="mark"></span></div>
<nav class="abs nav">
  <span>Home</span><span>About Us ▾</span><span>What We Offer ▾</span><span>Compare</span><span>FAQ</span><span>Contact</span>
</nav>
<div class="btn nav-cta">Request Free Market Analysis
  <svg width="14" height="12" viewBox="0 0 14 12" fill="none" stroke="#fff" stroke-width="1.6"><path d="M1 6h11M7 1l5 5-5 5"/></svg>
</div>

<!-- Hero -->
<div class="abs hero-photo" role="img" aria-label="Smiling doctor in a white coat with a stethoscope seated at a desk beside a brick wall"></div>
<div class="abs hero-copy">
  <h1><span>Start Your Own</span> Profitable Weight Loss Clinic!</h1>
  <p class="first">We are not a weight loss franchise – you are simply buying our business model, training and support for one low fee. Please read about us, look at what we offer and compare us to weight loss franchises in the marketplace.</p>
  <p>We offer you a free market analysis and sample break even analysis for your area.</p>
  <p><strong>We think you will be happy you found us!</strong></p>
</div>
<div class="btn hero-btn">Learn More</div>

<!-- What we offer -->
<h2 class="abs offer-title">What We Offer</h2>
<div class="abs card card-1" style="left:103px" role="img" aria-label="Business consultant reviewing documents with a doctor"><p>One-on-one business &amp; medical training</p></div>
<div class="abs card card-2" style="left:355px" role="img" aria-label="Presenter at a whiteboard during a marketing meeting"><p>Marketing &amp; Advertising Training</p></div>
<div class="abs card card-3" style="left:607px" role="img" aria-label="Measuring tape around a waist above blue jeans"><p>Diets, Patient Protocols &amp; Programs</p></div>
<div class="abs card card-4" style="left:861px" role="img" aria-label="Office worker reading at a desk with a computer"><p>Office &amp; Operations Manuals</p></div>

<!-- Welcome band -->
<div class="abs welcome"></div>
<div class="abs welcome-photo" role="img" aria-label="Patient on a video consultation with a doctor on a laptop"></div>
<div class="abs welcome-frame"></div>
<div class="abs welcome-copy">
  <div class="hi">Welcome there!</div>
  <h2>Start Your Own</h2>
  <div class="sub">WEIGHT LOSS &amp; WELLNESS CENTER</div>
  <p>Bright Vitality Centre now offers our model to you so you can add weight loss and wellness programs to your existing medical practice or open a stand alone weight loss and wellness center.</p>
  <p>We are not a weight loss franchise – you are simply buying our business model, training and support for one low fee. Please read about us, look at what we offer and compare us to weight loss franchises in the marketplace.</p>
  <p>We now offer you a free market analysis and sample break even analysis for your area. Please see our contact page.</p>
  <p><strong>We think you will be happy you found us!</strong></p>
</div>

<!-- Compare -->
<h2 class="abs compare-title">Compare</h2>
<ul class="abs checks">
  <li><svg width="15" height="15" viewBox="0 0 16 16"><circle cx="8" cy="8" r="8" fill="#c8202f"/><path d="M4.5 8.3l2.3 2.2 4.7-4.8" fill="none" stroke="#fff" stroke-width="1.8"/></svg>No franchise fees</li>
  <li><svg width="15" height="15" viewBox="0 0 16 16"><circle cx="8" cy="8" r="8" fill="#c8202f"/><path d="M4.5 8.3l2.3 2.2 4.7-4.8" fill="none" stroke="#fff" stroke-width="1.8"/></svg>No scope of practice limits</li>
  <li><svg width="15" height="15" viewBox="0 0 16 16"><circle cx="8" cy="8" r="8" fill="#c8202f"/><path d="M4.5 8.3l2.3 2.2 4.7-4.8" fill="none" stroke="#fff" stroke-width="1.8"/></svg>No territory fees</li>
  <li><svg width="15" height="15" viewBox="0 0 16 16"><circle cx="8" cy="8" r="8" fill="#c8202f"/><path d="M4.5 8.3l2.3 2.2 4.7-4.8" fill="none" stroke="#fff" stroke-width="1.8"/></svg>No convention fees</li>
  <li><svg width="15" height="15" viewBox="0 0 16 16"><circle cx="8" cy="8" r="8" fill="#c8202f"/><path d="M4.5 8.3l2.3 2.2 4.7-4.8" fill="none" stroke="#fff" stroke-width="1.8"/></svg>No monthly licensing fees</li>
  <li><svg width="15" height="15" viewBox="0 0 16 16"><circle cx="8" cy="8" r="8" fill="#c8202f"/><path d="M4.5 8.3l2.3 2.2 4.7-4.8" fill="none" stroke="#fff" stroke-width="1.8"/></svg>No % royalties</li>
  <li><svg width="15" height="15" viewBox="0 0 16 16"><circle cx="8" cy="8" r="8" fill="#c8202f"/><path d="M4.5 8.3l2.3 2.2 4.7-4.8" fill="none" stroke="#fff" stroke-width="1.8"/></svg>No % advertising fees</li>
  <li><svg width="15" height="15" viewBox="0 0 16 16"><circle cx="8" cy="8" r="8" fill="#c8202f"/><path d="M4.5 8.3l2.3 2.2 4.7-4.8" fill="none" stroke="#fff" stroke-width="1.8"/></svg>No mandatory vendors</li>
</ul>
<div class="btn compare-btn">Learn More</div>
<div class="abs compare-photo" role="img" aria-label="Woman in a white sports top and blue shorts measuring her waist with a tape"></div>

<!-- Get started -->
<div class="abs steps"></div>
<div class="abs easy">It’s Easy</div>
<h2 class="abs steps-title">GET STARTED TODAY</h2>

<div class="abs step" style="left:132px;top:2450px">
  <div class="disc"><span class="num">1</span>
    <svg width="40" height="34" viewBox="0 0 40 34" fill="none" stroke="#134a8e" stroke-width="3"><rect x="8" y="8" width="28" height="20" rx="2"/><path d="M8 9l14 10 14-10"/><path d="M3 6c0 8 3 14 9 18" stroke-linecap="round"/></svg>
  </div>
  <h3>Contact Us</h3>
  <p>Contact us for more<br>information on our model</p>
</div>
<svg class="abs" style="left:360px;top:2476px" width="146" height="28" viewBox="0 0 146 28" fill="none" stroke="#444" stroke-width="2"><path d="M2 16C40 4 100 2 138 14" stroke-dasharray="7 5"/><path d="M130 7l9 7-10 5"/></svg>

<div class="abs step" style="left:447px;top:2450px">
  <div class="disc"><span class="num">2</span>
    <svg width="40" height="38" viewBox="0 0 40 38" fill="none" stroke="#134a8e" stroke-width="3"><rect x="3" y="6" width="30" height="26" rx="2"/><path d="M3 13h30M10 2v8M26 2v8M9 19h4M16 19h4M9 25h4"/><circle cx="30" cy="29" r="7" fill="#fff"/><path d="M30 25v4h3"/></svg>
  </div>
  <h3>Visit Us</h3>
  <p>Schedule a time to visit<br>Atlanta and see our<br>clinics in action</p>
</div>
<svg class="abs" style="left:668px;top:2484px" width="146" height="28" viewBox="0 0 146 28" fill="none" stroke="#444" stroke-width="2"><path d="M2 12C40 24 100 22 138 8" stroke-dasharray="7 5"/><path d="M128 4l11 3-6 9"/></svg>

<div class="abs step" style="left:750px;top:2450px">
  <div class="disc"><span class="num">3</span>
    <svg width="44" height="38" viewBox="0 0 44 38" fill="none" stroke="#134a8e" stroke-width="3"><rect x="4" y="6" width="36" height="24" rx="2"/><path d="M16 36h12M22 30v6"/><circle cx="16" cy="16" r="3"/><path d="M10 25c1-4 11-4 12 0M26 14h9M26 20h7"/></svg>
  </div>
  <h3 style="margin-top:14px">Schedule a Webinar</h3>
  <p>Schedule your one-on-one<br>20 minute webinar more+</p>
</div>
<div class="btn steps-btn">Learn More</div>

<!-- Partners -->
<div class="abs" style="left:220px;top:2924px;width:92px;height:92px;border-radius:50%;background:#2d72a8" role="img" aria-label="Accreditation badge"></div>
<div class="abs" style="left:446px;top:2924px;width:72px;height:72px;border-radius:50%;background:#5a2e68" role="img" aria-label="Professional society badge"></div>
<div class="abs" style="left:425px;top:3006px;width:245px;height:10px;background:#b8a79a" role="img" aria-label="Professional society badge tagline band"></div>
<div class="abs" style="left:804px;top:2932px;width:142px;height:92px;background:#2b3f7a" role="img" aria-label="Medical academy membership badge"></div>

<!-- Contact -->
<div class="abs contact-photo" role="img" aria-label="Doctor in a white coat holding a bathroom scale"></div>
<div class="abs contact-panel"></div>
<div class="abs contact-kicker">Contact us</div>
<h2 class="abs contact-title">Today to Learn More</h2>
<div class="field" style="left:645px;top:3305px;width:219px">Name</div>
<div class="field" style="left:885px;top:3305px;width:220px">Email addresss</div>
<div class="field" style="left:645px;top:3366px;width:219px">Phone</div>
<div class="field" style="left:885px;top:3366px;width:220px">City/State</div>
<div class="field" style="left:645px;top:3427px;width:460px;height:111px">Message</div>
<div class="submit">SUBMIT</div>

<!-- Footer -->
<div class="abs footer"></div>
<div class="abs foot-brand"><span class="name">Bright Vitality<br>Centre</span><span class="mark"></span></div>

<div class="abs foot-h" style="left:424px;top:3722px">Contact Information</div>
<div class="abs foot-row" style="left:424px;top:3766px">
  <svg width="14" height="16" viewBox="0 0 24 24" fill="none" stroke="#fff" stroke-width="2" style="margin-top:3px"><path d="M12 22s7-7 7-12a7 7 0 0 0-14 0c0 5 7 12 7 12z"/><circle cx="12" cy="10" r="2.5"/></svg>
  <span>4410 Meadow Crest Road<br>Suite 210, Lakeview, GA<br>30190</span>
</div>
<div class="abs foot-row" style="left:424px;top:3850px;align-items:center">
  <svg width="16" height="16" viewBox="0 0 24 24" fill="none" stroke="#fff" stroke-width="2"><path d="M22 17v4a1 1 0 0 1-1 1A19 19 0 0 1 2 3a1 1 0 0 1 1-1h4l2 5-2.5 1.5a11 11 0 0 0 6 6L15 12l5 2z"/></svg>
  <span>877-555-0148</span>
</div>
<div class="abs foot-row" style="left:424px;top:3894px;align-items:center">
  <svg width="18" height="14" viewBox="0 0 24 18" fill="none" stroke="#fff" stroke-width="2"><rect x="1" y="1" width="22" height="16" rx="2"/><path d="M1 2l11 8 11-8"/></svg>
  <span>hello@slimpathcoaching.net</span>
</div>

<div class="abs foot-h" style="left:750px;top:3722px">QUICKLINKS</div>
<div class="abs quick" style="left:751px;top:3761px">Home<br>About Us<br>What We Offer<br>Compare<br>FAQ<br>Contact</div>

<div class="abs foot-h" style="left:969px;top:3722px">Connect With Us</div>
<div class="abs social" style="left:967px;top:3766px"><span></span><span></span><span></span></div>

<div class="abs copyright">© 2019 Bright Vitality Centre, Inc. All rights reserved</div>

</body>
</html>
```